Stationery Design Project

Letterhead with logo and address
Envelopes with Logo and address

The target market is start-ups and
small to medium businesses primarly located in China, with less than 20
employees. Please have designers use Yellow and Blue colors and our logo
attached. Looking fr the same format as the business card attached.
Updates

Reason: Designer has been delayed working on web design

Target Market(s)

Start-ups and small to medium size businesses

Industry/Entity Type

Business

Font styles to use
Sans Serif

Requirements
Must have
Nice to have
Should not have

```html
<!DOCTYPE html>
<html lang="en">
<head>
<meta charset="utf-8">
<title>NORVALE Stationery Set</title>
<link href="https://fonts.googleapis.com/css2?family=Arimo:wght@400;700&display=swap" rel="stylesheet">
<style>
  :root {
    --navy: #1a3b6d;
    --navy-dark: #16335f;
    --brand-blue: #2a6aa6;
    --brand-yellow: #f6c21c;
    --paper: #ffffff;
    --paper-grey: #e6e6e6;
    --rule: #6f86ad;
    --window-rule: #8a8a8a;
    --stage-left: #3c3c3e;
    --stage-right: #1d1c1c;
  }
  * { box-sizing: border-box; margin: 0; padding: 0; }
  html, body { width: 1200px; height: 1000px; overflow: hidden; }
  body {
    position: relative;
    font-family: "Arimo", Arial, sans-serif;
    background: linear-gradient(90deg, var(--stage-left) 0%, #2e2d2e 55%, var(--stage-right) 100%);
  }
  .sheet { position: absolute; box-shadow: 0 4px 14px rgba(0,0,0,.45); overflow: hidden; }

  /* Letterhead */
  .letterhead { left: 2px; top: 84px; width: 586px; height: 828px; background: var(--paper); }
  .letterhead__header { position: absolute; left: 0; top: 0; width: 100%; height: 121px; background: var(--navy); border-bottom: 2px solid var(--navy-dark); }
  .letterhead__footer-band { position: absolute; left: 0; bottom: 0; width: 100%; height: 26px; background: var(--navy); }

  /* Brand lockup */
  .brand { position: absolute; display: flex; flex-direction: column; align-items: center; }
  .brand__dot { border-radius: 50%; background: var(--brand-yellow); }
  .brand__name { color: var(--brand-blue); font-weight: 700; letter-spacing: 3px; margin-top: 8px; }
  .letterhead .brand { left: 60px; top: 10px; width: 88px; }
  .letterhead .brand__dot { width: 66px; height: 66px; }
  .letterhead .brand__name { font-size: 14px; margin-top: 12px; }

  .address { position: absolute; text-align: center; color: var(--navy); }
  .address__rule { height: 1px; background: var(--rule); margin: 0 auto; }
  .letterhead .address { left: 150px; top: 744px; width: 290px; font-size: 12px; line-height: 14px; }
  .letterhead .address__rule { width: 290px; margin-bottom: 16px; }

  /* Envelope front */
  .envelope-front { left: 623px; top: 260px; width: 577px; height: 305px; background: var(--navy); }
  .envelope-front .brand { left: 30px; top: 24px; width: 100px; }
  .envelope-front .brand__dot { width: 76px; height: 76px; }
  .envelope-front .brand__name { font-size: 16px; margin-top: 14px; }
  .address-window { position: absolute; left: 310px; top: 129px; width: 250px; height: 124px; background: var(--paper); padding: 66px 27px 0 28px; }
  .address-window__line { height: 1px; background: var(--window-rule); margin-bottom: 13px; }

  /* Envelope back */
  .envelope-back { left: 621px; top: 600px; width: 579px; height: 307px; background: var(--paper-grey); }
  .envelope-back__flap { position: absolute; left: 0; top: 0; width: 100%; height: 86px; background: var(--navy); }
  .envelope-back .brand { left: 257px; top: 98px; width: 100px; }
  .envelope-back .brand__dot { width: 78px; height: 78px; }
  .envelope-back .brand__name { font-size: 16px; margin-top: 18px; color: #1d4f86; }
  .envelope-back .address { left: 199px; top: 261px; width: 217px; font-size: 9px; line-height: 11px; }
  .envelope-back .address__rule { width: 217px; margin-bottom: 12px; }
</style>
</head>
<body>

<section class="sheet letterhead" aria-label="Letterhead">
  <header class="letterhead__header">
    <div class="brand">
      <span class="brand__dot"></span>
      <span class="brand__name">NORVALE</span>
    </div>
  </header>
  <footer class="address">
    <div class="address__rule"></div>
    <p>Linqiao Road 58, suite 210-212</p>
    <p>Minhe Dist. Hangzhou</p>
  </footer>
  <div class="letterhead__footer-band"></div>
</section>

<section class="sheet envelope-front" aria-label="Envelope front">
  <div class="brand">
    <span class="brand__dot"></span>
    <span class="brand__name">NORVALE</span>
  </div>
  <div class="address-window">
    <div class="address-window__line"></div>
    <div class="address-window__line"></div>
    <div class="address-window__line"></div>
    <div class="address-window__line"></div>
  </div>
</section>

<section class="sheet envelope-back" aria-label="Envelope back">
  <div class="envelope-back__flap"></div>
  <div class="brand">
    <span class="brand__dot"></span>
    <span class="brand__name">NORVALE</span>
  </div>
  <footer class="address">
    <div class="address__rule"></div>
    <p>Linqiao Road 58, suite 210-212</p>
    <p>Minhe Dist. Hangzhou</p>
  </footer>
</section>

</body>
</html>
```